Awesome Business Card Design needed!

Hey there.
I'm looking for a simple but awesome business card design.
Type of company: Online advertisement agency
(please don't use the typical business people or statistics images on the card)
The front has to display the business name
and possibly some sort of logo ( perhaps something with the two M's of the biz name )
And the back of the card should say:
Name
Phone
Email
Let your imagination flow.
here are some designs that I like and that you can use as inspiration.
Simple but Awesome
http://images.pixelvantor.net/designs/55128_877673_43091_thumbnail.jpg
http://images.pixelvantor.net/designs/37714_747642_40106_image.jpg
http://images.pixelvantor.net/designs/55128_877673_43091_image.jpg
http://images.pixelvantor.net/designs/51321_781878_43091_image.jpg
http://images.pixelvantor.net/designs/33378_399063_15912_image.jpg
http://images.pixelvantor.net/designs/2337_271604_9495_image.jpg
good luck

```html
<!DOCTYPE html>
<html lang="en">
<head>
<meta charset="utf-8">
<title>Vantello Media – Business Card</title>
<link href="https://fonts.googleapis.com/css2?family=Open+Sans:wght@400;600&family=Libre+Baskerville:wght@700&display=swap" rel="stylesheet">
<style>
  :root {
    --bg-top: #141516;
    --bg-bottom: #f2f2f2;
    --card: #121314;
    --card-deep: #0b0b0c;
    --text-light: #f4f4f4;
    --logo-grey: #cfd3d6;
    --swoosh-white: #ffffff;
    --swoosh-cyan: #7fe6ea;
  }
  html, body {
    margin: 0;
    padding: 0;
    width: 1200px;
    height: 1200px;
    overflow: hidden;
  }
  body {
    background: linear-gradient(180deg, var(--bg-top) 0%, #3d4142 45%, #9a9c9c 75%, var(--bg-bottom) 100%);
    position: relative;
    font-family: "Open Sans", Arial, sans-serif;
  }
  .card {
    position: absolute;
    background: linear-gradient(180deg, var(--card) 0%, var(--card-deep) 100%);
    box-shadow: 0 4px 10px rgba(0,0,0,0.55);
    overflow: hidden;
  }
  .card svg {
    position: absolute;
    inset: 0;
    width: 100%;
    height: 100%;
  }
  .card-back {
    left: 588px;
    top: 108px;
    width: 532px;
    height: 304px;
  }
  .card-front {
    left: 50px;
    top: 388px;
    width: 750px;
    height: 427px;
  }
  .brand-name {
    position: absolute;
    margin: 0;
    font-family: "Open Sans", Arial, sans-serif;
    font-weight: 600;
    color: var(--logo-grey);
    letter-spacing: 0.5px;
    white-space: nowrap;
  }
  .card-front .brand-name {
    left: 0;
    right: 0;
    top: 135px;
    text-align: center;
    font-size: 48px;
  }
  .card-back .brand-name {
    right: 22px;
    top: 22px;
    font-size: 20px;
  }
  .tagline {
    position: absolute;
    left: 0;
    right: 0;
    top: 385px;
    margin: 0;
    text-align: center;
    font-family: "Libre Baskerville", Georgia, serif;
    font-weight: 700;
    font-size: 12.5px;
    color: var(--text-light);
  }
  .contact {
    position: absolute;
    right: 20px;
    top: 166px;
    margin: 0;
    text-align: center;
    color: var(--text-light);
    font-size: 18px;
    line-height: 25.5px;
    font-style: normal;
  }
  .contact span { display: block; }
</style>
</head>
<body>

  <section class="card card-back" aria-label="Business card back">
    <svg viewBox="0 0 532 304" aria-hidden="true">
      <defs>
        <linearGradient id="swoosh-back" x1="0" y1="0" x2="1" y2="0">
          <stop offset="0" stop-color="#ffffff"/>
          <stop offset="0.45" stop-color="#e8f6f6"/>
          <stop offset="0.8" stop-color="#7fe6ea"/>
          <stop offset="1" stop-color="#9ff0f2"/>
        </linearGradient>
      </defs>
      <path d="M0 54 C160 62 300 82 400 88 S 500 86 532 84" fill="none" stroke="url(#swoosh-back)" stroke-width="3"/>
      <path d="M0 242 C160 244 300 262 400 266 S 500 262 532 258" fill="none" stroke="url(#swoosh-back)" stroke-width="3"/>
    </svg>
    <p class="brand-name">Vantello Media</p>
    <address class="contact">
      <span class="contact-name">Daniel Reyes</span>
      <span class="contact-phone">phone: 00385 1 555 0142</span>
      <span class="contact-email">daniel@vantello.com</span>
    </address>
  </section>

  <section class="card card-front" aria-label="Business card front">
    <svg viewBox="0 0 750 427" aria-hidden="true">
      <defs>
        <linearGradient id="swoosh-front" x1="0" y1="0" x2="1" y2="0">
          <stop offset="0" stop-color="#ffffff"/>
          <stop offset="0.3" stop-color="#dff3f3"/>
          <stop offset="0.6" stop-color="#7fe6ea"/>
          <stop offset="1" stop-color="#ffffff"/>
        </linearGradient>
      </defs>
      <path d="M0 342 C200 348 380 362 500 360 S 700 346 750 334 L750 427 L0 427 Z" fill="#0a0a0a"/>
      <path d="M0 340 C200 346 380 360 500 358 S 700 344 750 332" fill="none" stroke="url(#swoosh-front)" stroke-width="3.5"/>
    </svg>
    <p class="brand-name">Vantello Media</p>
    <p class="tagline">online advertisement agency</p>
  </section>

</body>
</html>
```